Update Dulmar & Co Powerpoint to Quillmere Partnership

Hi, about 2 years ago I had a great Powerpoint template produced for my business called Dulmar & Co. We have now changed the company name and logo to Quillmere Partnership and I would like you to update the presentation template pages to the new logo and design.

I attach:

1) The original Powerpoint presentation that was produced for Dulmar
2) The new Quillmere Partnership logo files
3) The initial Powerpoint presentation format that my UK designer has done to give you an idea of their approach
4) The Font files (Red Hat Display - medium)

It would be great to receive the new PP template by Tuesday 22nd July.

Please message me if you have any questions.
Thanks
Ned

```html
<!DOCTYPE html>
<html lang="en">
<head>
<meta charset="utf-8">
<title>Quillmere Partnership – Presentation Template</title>
<link href="https://fonts.googleapis.com/css2?family=Red+Hat+Display:wght@400;500;600;700;800&display=swap" rel="stylesheet">
<style>
  :root{
    --board:#3b3b3b;
    --ink:#0a3035;
    --teal:#1f5558;
    --teal-soft:#2d6a6c;
    --orange:#e2550e;
    --paper:#ffffff;
    --muted:#4f6264;
    --rule:#d5dcdc;
    --mist:#c9d6d6;
  }
  *{box-sizing:border-box;margin:0;padding:0}
  html,body{width:987px;height:1200px;overflow:hidden;background:var(--board)}
  body{font-family:"Red Hat Display",Arial,sans-serif;color:var(--ink)}
  .board{position:relative;width:987px;height:1200px;background:var(--board);overflow:hidden}
  .slide{position:absolute;width:298px;height:167px;overflow:hidden}
  .dark{background:var(--ink);color:var(--paper)}
  .light{background:var(--paper);color:var(--ink)}
  .abs{position:absolute}
  .tiny{font-size:2.6px;line-height:1.4;font-weight:400}
  .dark .tiny{color:#dfe8e8}
  .light .tiny{color:var(--muted)}
  .center{text-align:center}
  .heading{font-size:9.5px;font-weight:700;line-height:1.1}
  .photo{background:linear-gradient(135deg,#d9d4cc 0%,#9aa3a4 45%,#4c5a5d 100%)}
  .photo.hands{background:linear-gradient(140deg,#efe9e2 0%,#b08a6c 45%,#5a3e30 100%)}

  /* brand */
  .brand{display:flex;align-items:center;gap:3px}
  .brand-mark{width:5px;height:5px;background:var(--orange)}
  .brand-name{font-weight:600;line-height:1}
  .brand-name .word{display:block;font-size:11px}
  .brand-name .sub{display:block;font-size:3.6px;letter-spacing:.7px;margin-top:1px}
  .mini-brand{position:absolute;top:6px;right:8px;display:flex;align-items:center;gap:1.5px;padding:1.5px 2px;background:var(--paper);color:var(--ink)}
  .mini-brand .brand-mark{width:3.5px;height:3.5px}
  .mini-brand .brand-name .word{font-size:5px}
  .mini-brand .brand-name .sub{font-size:1.6px;letter-spacing:.3px;margin-top:.3px}

  /* footer */
  .foot{position:absolute;left:11px;right:8px;bottom:7px;display:flex;align-items:center;gap:3px;font-size:2.3px}
  .light .foot{color:var(--muted)}
  .dark .foot{color:#9fb3b3}
  .foot .line{flex:1;height:.5px;background:var(--teal)}
  .dark .foot .line{background:#3f6a6c}
  .foot .page{width:5px;height:5px;border-radius:50%;background:var(--teal);color:var(--paper);display:flex;align-items:center;justify-content:center;font-size:2.4px;font-weight:700}

  /* cover */
  .cover-title{left:26px;top:62px;font-size:14.5px;line-height:1.05;font-weight:800}
  .cover-sub{left:26px;top:106px;font-size:6px;font-weight:400;color:#dfe8e8}
  .cover-rule{left:26px;top:141px;width:9px;height:.8px;background:var(--orange)}
  .cover-date{left:26px;top:145px;font-size:3px;color:#b9c9c9}

  /* toc */
  .toc-num{width:17px;height:17px;border:.8px solid var(--orange);display:flex;align-items:center;justify-content:center;font-size:10px;font-weight:400;color:var(--ink)}
  .toc-label{font-size:5px;font-weight:700}
  .toc-rule{height:.4px;background:var(--rule)}

  /* lists */
  .num{width:13px;height:13px;border-radius:50%;background:var(--orange);color:var(--paper);display:flex;align-items:center;justify-content:center;font-size:6px;font-weight:600}
  .num.ink{background:var(--ink)}
  .desc-title{font-size:3px;font-weight:700}
  .desc{font-size:2.6px;line-height:1.35}
  .bullet-col .col-head{font-size:4px;font-weight:700;margin-bottom:6px}
  .bullet{display:flex;gap:4px;align-items:flex-start;padding:3px 0 4px;border-bottom:.4px solid var(--rule);font-size:2.5px;line-height:1.35;height:17.5px}
  .dark .bullet{border-bottom:none}
  .bullet .dot{flex:none;width:4px;height:4px;border-radius:50%;border:.5px solid currentColor;margin-top:.5px}
  .bullet .dot.hot{background:var(--orange);border-color:var(--orange)}

  /* cards */
  .card{position:absolute;top:43px;width:52px;height:96px;background:var(--teal);color:var(--paper);border-radius:1.5px;text-align:center;padding:8px 3px 0}
  .icon{width:13px;height:13px;border-radius:50%;background:var(--paper);margin:0 auto;display:flex;align-items:center;justify-content:center}
  .icon svg{width:8px;height:8px}
  .card .card-head{font-size:6px;font-weight:600;margin:5px 0 2px}
  .card .tiny{color:#e4eded}
  .feat{position:absolute;width:80px;text-align:center}
  .feat .icon{background:var(--paper)}
  .feat .feat-head{font-size:6px;font-weight:600;margin:4px 0 1px}

  /* image cards */
  .pcard{position:absolute;top:49px;width:71px;height:97px;background:var(--paper);border-radius:2px;overflow:hidden;padding:0 6px}
  .pcard .photo{height:43px;margin:0 -6px 6px}
  .pcard .pc-head{font-size:4px;font-weight:700;margin-bottom:3px}
  .pcard .row{display:flex;gap:3px;font-size:2.3px;line-height:1.35;color:var(--muted);margin-bottom:3px}
  .pcard .row .dot{flex:none;width:4px;height:4px;border-radius:50%;background:var(--orange)}

  /* table */
  .grid{position:absolute;left:17px;top:47px;width:260px;border-collapse:collapse;font-size:2.3px}
  .grid th{background:var(--ink);color:var(--paper);font-size:3.2px;font-weight:600;height:11px;padding:0 2px;border:.4px solid var(--rule)}
  .grid th:first-child{text-align:left}
  .grid td{height:15px;padding:1px 2px;border:.4px solid var(--rule);color:var(--muted);line-height:1.3;vertical-align:middle}
  .grid tr:nth-child(even) td{background:#f1f3f3}
  .grid td.rowhead{color:var(--orange);font-size:3.4px;font-weight:500}

  /* thanks */
  .thanks{left:176px;top:52px;font-size:27px;line-height:.95;font-weight:800;text-align:center}
  .contact{display:flex;align-items:center;gap:4px;font-size:3.5px;color:#dfe8e8;margin-bottom:6px}
  .contact svg{width:6px;height:6px}
</style>
</head>
<body>
<main class="board">

  <!-- Cover with illustration -->
  <section class="slide dark" style="left:28px;top:37px">
    <div class="abs brand" style="left:25px;top:20px"><span class="brand-mark"></span><span class="brand-name"><span class="word">Quillmere</span><span class="sub">PARTNERSHIP</span></span></div>
    <h1 class="abs cover-title">Presentation Title<br>Goes Here</h1>
    <p class="abs cover-sub">Subtitle of Presentation Goes Here</p>
    <div class="abs cover-rule"></div>
    <p class="abs cover-date">20 July 2025</p>
    <div class="abs" role="img" aria-label="Illustration of two people shaking hands in front of a large signed document" style="left:172px;top:16px;width:114px;height:120px;background:linear-gradient(160deg,#1c4a4d 0%,#2c6164 60%,#0a3035 100%)"></div>
    <div class="abs" style="left:166px;top:138px;width:122px;height:.5px;background:#dfe8e8"></div>
  </section>

  <!-- Cover plain -->
  <section class="slide dark" style="left:345px;top:37px">
    <div class="abs brand" style="left:25px;top:20px"><span class="brand-mark"></span><span class="brand-name"><span class="word">Quillmere</span><span class="sub">PARTNERSHIP</span></span></div>
    <h1 class="abs cover-title">Presentation Title<br>Goes Here</h1>
    <p class="abs cover-sub">Subtitle of Presentation Goes Here</p>
    <div class="abs cover-rule"></div>
    <p class="abs cover-date">20 July 2025</p>
  </section>

  <!-- Table of contents -->
  <section class="slide light" style="left:661px;top:37px">
    <h2 class="abs center" style="left:0;right:0;top:17px;font-size:8.5px;font-weight:700">Table of Contents</h2>
    <div class="abs" style="left:142px;top:30px;width:14px;height:.6px;background:var(--teal)"></div>
    <div class="abs toc-num" style="left:42px;top:49px">1</div><p class="abs toc-label" style="left:63px;top:55px">Title Goes Here</p>
    <div class="abs toc-num" style="left:159px;top:49px">2</div><p class="abs toc-label" style="left:180px;top:55px">Title Goes Here</p>
    <div class="abs toc-rule" style="left:63px;top:75px;width:76px"></div><div class="abs toc-rule" style="left:180px;top:75px;width:76px"></div>
    <div class="abs toc-num" style="left:42px;top:83px">3</div><p class="abs toc-label" style="left:63px;top:89px">Title Goes Here</p>
    <div class="abs toc-num" style="left:159px;top:83px">4</div><p class="abs toc-label" style="left:180px;top:89px">Title Goes Here</p>
    <div class="abs toc-rule" style="left:63px;top:109px;width:76px"></div><div class="abs toc-rule" style="left:180px;top:109px;width:76px"></div>
    <div class="abs toc-num" style="left:42px;top:117px">5</div><p class="abs toc-label" style="left:63px;top:123px">Title Goes Here</p>
    <div class="abs toc-num" style="left:159px;top:117px">6</div><p class="abs toc-label" style="left:180px;top:123px">Title Goes Here</p>
    <footer class="foot"><span>© Quillmere 2025. All Rights Reserved.</span><span class="line"></span><span class="page">2</span></footer>
  </section>

  <!-- Intro with brand -->
  <section class="slide light" style="left:28px;top:225px">
    <h2 class="abs heading" style="left:29px;top:37px;font-size:10px">Heading Goes Here</h2>
    <div class="abs" style="left:29px;top:61px;width:110px">
      <p class="tiny">Add a short summary of the topic here so the reader can follow the main idea. Keep each line brief and clear for the audience.</p>
      <p class="tiny" style="margin-top:4px">Use this second block to give more detail on the point above. Add facts, short notes and a clear message that helps the reader see why this part of the talk matters to them today.</p>
      <p class="tiny" style="margin-top:4px">Close the section with a final short note that links to the next slide and keeps the story moving.</p>
    </div>
    <div class="abs brand" style="left:176px;top:64px;color:var(--ink)"><span class="brand-mark" style="width:8px;height:8px"></span><span class="brand-name"><span class="word" style="font-size:18px">Quillmere</span><span class="sub" style="font-size:5px;letter-spacing:1.4px">PARTNERSHIP</span></span></div>
    <footer class="foot"><span>© Quillmere 2025. All Rights Reserved.</span><span class="line"></span><span class="page">3</span></footer>
  </section>

  <!-- Two images with text -->
  <section class="slide light" style="left:345px;top:225px">
    <div class="abs dark" style="left:0;top:0;width:298px;height:79px"></div>
    <h2 class="abs heading" style="left:17px;top:18px;color:var(--paper)">Heading Goes Here</h2>
    <div class="abs photo" role="img" aria-label="Photo of a tablet showing a chart beside a handshake" style="left:17px;top:44px;width:126px;height:46px"></div>
    <div class="abs photo hands" role="img" aria-label="Photo of hands reviewing a printed report" style="left:156px;top:44px;width:126px;height:46px"></div>
    <h3 class="abs" style="left:17px;top:100px;font-size:7px;font-weight:500;color:var(--orange)">Heading Goes Here</h3>
    <p class="abs tiny" style="left:17px;top:110px;width:112px;font-size:3px">Add a short summary of this topic here. Give the reader a clear idea of the point and why it matters, then close with a brief note that leads into the next part of the slide.</p>
    <h3 class="abs" style="left:156px;top:100px;font-size:7px;font-weight:500;color:var(--orange)">Heading Goes Here</h3>
    <p class="abs tiny" style="left:156px;top:110px;width:112px;font-size:3px">Add a short summary of this topic here. Give the reader a clear idea of the point and why it matters, then close with a brief note that leads into the next part of the slide.</p>
    <footer class="foot"><span>© Quillmere 2025. All Rights Reserved.</span><span class="line"></span><span class="page">4</span></footer>
  </section>

  <!-- Two bullet columns dark -->
  <section class="slide dark" style="left:661px;top:225px">
    <div class="mini-brand"><span class="brand-mark"></span><span class="brand-name"><span class="word">Quillmere</span><span class="sub">PARTNERSHIP</span></span></div>
    <h2 class="abs heading center" style="left:0;right:0;top:13px">Heading Goes Here</h2>
    <p class="abs tiny center" style="left:48px;width:202px;top:27px">Add a short summary of the slide here so the reader knows what follows. Keep it to two brief lines and close with a clear note on the key idea.</p>
    <div class="abs bullet-col" style="left:42px;top:54px;width:100px">
      <p class="col-head">Heading Goes Here</p>
      <div class="bullet"><span class="dot"></span><span>Add a key point here in one short line and a brief note below it.</span></div>
      <div class="bullet"><span class="dot hot"></span><span>Add one more point here in a single line.</span></div>
      <div class="bullet"><span class="dot"></span><span>Add a key point here in one short line and a brief note below it.</span></div>
      <div class="bullet"><span class="dot hot"></span><span>Add a key point here in one short line and a brief note below it.</span></div>
      <div class="bullet"><span class="dot"></span><span>Add a key point here in one short line and a brief note below it.</span></div>
    </div>
    <div class="abs bullet-col" style="left:172px;top:54px;width:100px">
      <p class="col-head">Heading Goes Here</p>
      <div class="bullet"><span class="dot"></span><span>Add a key point here in one short line and a brief note below it.</span></div>
      <div class="bullet"><span class="dot hot"></span><span>Add one more point here in a single line.</span></div>
      <div class="bullet"><span class="dot"></span><span>Add a key point here in one short line and a brief note below it.</span></div>
      <div class="bullet"><span class="dot hot"></span><span>Add a key point here in one short line and a brief note below it.</span></div>
      <div class="bullet"><span class="dot"></span><span>Add a key point here in one short line and a brief note below it.</span></div>
    </div>
    <footer class="foot"><span>© Quillmere 2025. All Rights Reserved.</span><span class="line"></span><span class="page">5</span></footer>
  </section>

  <!-- Image panel with five steps -->
  <section class="slide light" style="left:28px;top:412px">
    <div class="abs dark" style="left:0;top:0;width:149px;height:167px"></div>
    <h2 class="abs heading" style="left:21px;top:21px;color:var(--paper)">Heading Goes Here</h2>
    <p class="abs tiny" style="left:21px;top:36px;width:100px;color:#dfe8e8">Add a short summary of the slide here so the reader can follow the key idea and see why it matters today.</p>
    <div class="abs photo hands" role="img" aria-label="Photo of hands pointing at a printed document" style="left:21px;top:63px;width:117px;height:86px"></div>
    <div class="mini-brand"><span class="brand-mark"></span><span class="brand-name"><span class="word">Quillmere</span><span class="sub">PARTNERSHIP</span></span></div>
    <div class="abs" style="left:173px;top:21px;width:110px">
      <div style="display:flex;gap:6px;height:28.8px"><span class="num">1</span><div><p class="desc-title">Description Text</p><p class="desc" style="color:var(--muted)">Add a short line about this point here and a brief note.</p></div></div>
      <div style="display:flex;gap:6px;height:28.8px"><span class="num">2</span><div><p class="desc-title">Description Text</p><p class="desc" style="color:var(--muted)">Add a short line about this point here and a brief note.</p></div></div>
      <div style="display:flex;gap:6px;height:28.8px"><span class="num">3</span><div><p class="desc-title">Description Text</p><p class="desc" style="color:var(--muted)">Add a short line about this point here and a brief note.</p></div></div>
      <div style="display:flex;gap:6px;height:26px"><span class="num">4</span><div><p class="desc-title">Description Text</p><p class="desc" style="color:var(--muted)">Add a short line about this point here and a brief note.</p></div></div>
      <div style="display:flex;gap:6px"><span class="num">5</span><div><p class="desc-title">Description Text</p><p class="desc" style="color:var(--muted)">Add a short line about this point here and a brief note.</p></div></div>
    </div>
    <footer class="foot"><span style="color:#9fb3b3">© Quillmere 2025. All Rights Reserved.</span><span class="line"></span><span class="page">6</span></footer>
  </section>

  <!-- Five cards -->
  <section class="slide light" style="left:345px;top:412px">
    <div class="mini-brand"><span class="brand-mark"></span><span class="brand-name"><span class="word">Quillmere</span><span class="sub">PARTNERSHIP</span></span></div>
    <h2 class="abs heading center" style="left:0;right:0;top:18px">Heading Goes Here</h2>
    <div class="card" style="left:9px"><div class="icon"><svg viewBox="0 0 16 16"><circle cx="8" cy="5.5" r="3" fill="#1f5558"/><path d="M2.5 15a5.5 5.5 0 0 1 11 0z" fill="#1f5558"/></svg></div><p class="card-head">Heading</p><p class="tiny">Add a short note about this heading here to explain the point in a clear way for the reader.</p><p class="tiny" style="margin-top:3px">Add one more brief line here to close.</p></div>
    <div class="card" style="left:66px"><div class="icon"><svg viewBox="0 0 16 16"><circle cx="8" cy="8" r="6" fill="none" stroke="#1f5558" stroke-width="1.6"/><path d="M2 8h12M8 2c-3 3-3 9 0 12M8 2c3 3 3 9 0 12" fill="none" stroke="#1f5558" stroke-width="1.2"/></svg></div><p class="card-head">Heading</p><p class="tiny">Add a short note about this heading here to explain the point in a clear way for the reader.</p><p class="tiny" style="margin-top:3px">Add one more brief line here to close.</p></div>
    <div class="card" style="left:123px"><div class="icon"><svg viewBox="0 0 16 16"><path d="M4 2h8v4a4 4 0 0 1-8 0z" fill="#1f5558"/><path d="M7 10h2v3H7zM5 13h6v1.5H5z" fill="#1f5558"/></svg></div><p class="card-head">Heading</p><p class="tiny">Add a short note about this heading here to explain the point in a clear way for the reader.</p><p class="tiny" style="margin-top:3px">Add one more brief line here to close.</p></div>
    <div class="card" style="left:180px"><div class="icon"><svg viewBox="0 0 16 16"><rect x="2" y="5" width="12" height="9" rx="1" fill="#1f5558"/><path d="M6 5V3h4v2" fill="none" stroke="#1f5558" stroke-width="1.4"/></svg></div><p class="card-head">Heading</p><p class="tiny">Add a short note about this heading here to explain the point in a clear way for the reader.</p><p class="tiny" style="margin-top:3px">Add one more brief line here to close.</p></div>
    <div class="card" style="left:237px"><div class="icon"><svg viewBox="0 0 16 16"><circle cx="8" cy="8" r="6" fill="none" stroke="#1f5558" stroke-width="1.6"/><path d="M8 4.5V8l2.5 1.5" fill="none" stroke="#1f5558" stroke-width="1.4"/></svg></div><p class="card-head">Heading</p><p class="tiny">Add a short note about this heading here to explain the point in a clear way for the reader.</p><p class="tiny" style="margin-top:3px">Add one more brief line here to close.</p></div>
    <footer class="foot"><span>© Quillmere 2025. All Rights Reserved.</span><span class="line"></span><span class="page">7</span></footer>
  </section>

  <!-- Image left, three steps -->
  <section class="slide light" style="left:661px;top:412px">
    <div class="abs dark" style="left:0;top:0;width:140px;height:167px"></div>
    <div class="abs photo hands" role="img" aria-label="Photo of hands reviewing a printed report at a desk" style="left:20px;top:24px;width:101px;height:118px"></div>
    <div class="mini-brand"><span class="brand-mark"></span><span class="brand-name"><span class="word">Quillmere</span><span class="sub">PARTNERSHIP</span></span></div>
    <h2 class="abs heading" style="left:163px;top:27px">Heading Goes Here</h2>
    <p class="abs tiny" style="left:163px;top:42px;width:96px">Add a short summary of the slide here so the reader can follow the key idea and see why it matters today.</p>
    <div class="abs" style="left:163px;top:72px;width:110px">
      <div style="display:flex;gap:6px;height:29px"><span class="num">1</span><div><p class="desc-title">Description Text</p><p class="desc" style="color:var(--muted)">Add a short line about this point here and a brief note.</p></div></div>
      <div style="display:flex;gap:6px;height:29px"><span class="num">2</span><div><p class="desc-title">Description Text</p><p class="desc" style="color:var(--muted)">Add a short line about this point here and a brief note.</p></div></div>
      <div style="display:flex;gap:6px"><span class="num">3</span><div><p class="desc-title">Description Text</p><p class="desc" style="color:var(--muted)">Add a short line about this point here and a brief note.</p></div></div>
    </div>
    <footer class="foot"><span style="color:#9fb3b3">© Quillmere 2025. All Rights Reserved.</span><span class="line"></span><span class="page">8</span></footer>
  </section>

  <!-- Six features dark -->
  <section class="slide dark" style="left:28px;top:600px">
    <div class="mini-brand"><span class="brand-mark"></span><span class="brand-name"><span class="word">Quillmere</span><span class="sub">PARTNERSHIP</span></span></div>
    <h2 class="abs heading center" style="left:0;right:0;top:16px">Heading Goes Here</h2>
    <div class="feat" style="left:18px;top:48px"><div class="icon"><svg viewBox="0 0 16 16"><circle cx="8" cy="5.5" r="3" fill="#1f5558"/><path d="M2.5 15a5.5 5.5 0 0 1 11 0z" fill="#1f5558"/></svg></div><p class="feat-head">Heading</p><p class="tiny">Add a short note here about<br>this key point in brief.</p></div>
    <div class="feat" style="left:106px;top:48px"><div class="icon"><svg viewBox="0 0 16 16"><circle cx="8" cy="8" r="6" fill="none" stroke="#1f5558" stroke-width="1.6"/><path d="M2 8h12M8 2c-3 3-3 9 0 12M8 2c3 3 3 9 0 12" fill="none" stroke="#1f5558" stroke-width="1.2"/></svg></div><p class="feat-head">Heading</p><p class="tiny">Add a short note here about<br>this key point in brief.</p></div>
    <div class="feat" style="left:196px;top:48px"><div class="icon"><svg viewBox="0 0 16 16"><path d="M4 2h8v4a4 4 0 0 1-8 0z" fill="#1f5558"/><path d="M7 10h2v3H7zM5 13h6v1.5H5z" fill="#1f5558"/></svg></div><p class="feat-head">Heading</p><p class="tiny">Add a short note here about<br>this key point in brief.</p></div>
    <div class="feat" style="left:18px;top:102px"><div class="icon"><svg viewBox="0 0 16 16"><rect x="2" y="3" width="12" height="11" rx="1" fill="none" stroke="#1f5558" stroke-width="1.4"/><path d="M2 6.5h12M5 9h2M9 9h2M5 11.5h2M9 11.5h2" stroke="#1f5558" stroke-width="1.2"/></svg></div><p class="feat-head">Heading</p><p class="tiny">Add a short note here about<br>this key point in brief.</p></div>
    <div class="feat" style="left:106px;top:102px"><div class="icon"><svg viewBox="0 0 16 16"><rect x="2" y="5" width="12" height="9" rx="1" fill="#1f5558"/><path d="M6 5V3h4v2" fill="none" stroke="#1f5558" stroke-width="1.4"/></svg></div><p class="feat-head">Heading</p><p class="tiny">Add a short note here about<br>this key point in brief.</p></div>
    <div class="feat" style="left:196px;top:102px"><div class="icon"><svg viewBox="0 0 16 16"><circle cx="8" cy="8" r="6" fill="none" stroke="#1f5558" stroke-width="1.6"/><path d="M8 4.5V8l2.5 1.5" fill="none" stroke="#1f5558" stroke-width="1.4"/></svg></div><p class="feat-head">Heading</p><p class="tiny">Add a short note here about<br>this key point in brief.</p></div>
    <footer class="foot"><span>© Quillmere 2025. All Rights Reserved.</span><span class="line"></span><span class="page">9</span></footer>
  </section>

  <!-- Two bullet columns light -->
  <section class="slide light" style="left:345px;top:600px">
    <div class="mini-brand"><span class="brand-mark"></span><span class="brand-name"><span class="word">Quillmere</span><span class="sub">PARTNERSHIP</span></span></div>
    <h2 class="abs heading center" style="left:0;right:0;top:13px">Heading Goes Here</h2>
    <p class="abs tiny center" style="left:48px;width:202px;top:27px">Add a short summary of the slide here so the reader knows what follows. Keep it to two brief lines and close with a clear note on the key idea.</p>
    <div class="abs bullet-col" style="left:42px;top:54px;width:100px">
      <p class="col-head">Heading Goes Here</p>
      <div class="bullet"><span class="dot"></span><span>Add a key point here in one short line and a brief note below it.</span></div>
      <div class="bullet"><span class="dot hot"></span><span>Add one more point here in a single line.</span></div>
      <div class="bullet"><span class="dot"></span><span>Add a key point here in one short line and a brief note below it.</span></div>
      <div class="bullet"><span class="dot hot"></span><span>Add a key point here in one short line and a brief note below it.</span></div>
      <div class="bullet" style="border-bottom:none"><span class="dot"></span><span>Add a key point here in one short line and a brief note below it.</span></div>
    </div>
    <div class="abs bullet-col" style="left:172px;top:54px;width:100px">
      <p class="col-head">Heading Goes Here</p>
      <div class="bullet"><span class="dot"></span><span>Add a key point here in one short line and a brief note below it.</span></div>
      <div class="bullet"><span class="dot hot"></span><span>Add one more point here in a single line.</span></div>
      <div class="bullet"><span class="dot"></span><span>Add a key point here in one short line and a brief note below it.</span></div>
      <div class="bullet"><span class="dot hot"></span><span>Add a key point here in one short line and a brief note below it.</span></div>
      <div class="bullet" style="border-bottom:none"><span class="dot"></span><span>Add a key point here in one short line and a brief note below it.</span></div>
    </div>
    <footer class="foot"><span>© Quillmere 2025. All Rights Reserved.</span><span class="line"></span><span class="page">10</span></footer>
  </section>

  <!-- Banner with text -->
  <section class="slide light" style="left:661px;top:600px">
    <div class="abs" role="img" aria-label="Tinted photo of a desk with documents and a pen" style="left:0;top:0;width:298px;height:79px;background:linear-gradient(120deg,#0d3a3f 0%,#1f5558 55%,#12424a 100%)"></div>
    <div class="mini-brand"><span class="brand-mark"></span><span class="brand-name"><span class="word">Quillmere</span><span class="sub">PARTNERSHIP</span></span></div>
    <h2 class="abs center" style="left:0;right:0;top:48px;font-size:11.5px;font-weight:600;color:var(--paper)">Heading Goes Here</h2>
    <p class="abs tiny center" style="left:20px;width:258px;top:100px">Add a short summary of the section here so the reader can follow the key idea. Keep the tone clear and the lines brief, then add one more note to round off this first block of text for the page.</p>
    <p class="abs tiny center" style="left:20px;width:258px;top:113px">Use this second block to give more detail on the topic. Add facts, short notes and a clear message that helps the reader see why this part matters. Keep each line the same length as the block above so the text sits well on the page and reads with ease from start to end of the slide.</p>
    <footer class="foot"><span>© Quillmere 2025. All Rights Reserved.</span><span class="line"></span><span class="page">11</span></footer>
  </section>

  <!-- Three image cards -->
  <section class="slide light" style="left:28px;top:787px">
    <div class="abs dark" style="left:0;top:100px;width:298px;height:67px"></div>
    <div class="mini-brand"><span class="brand-mark"></span><span class="brand-name"><span class="word">Quillmere</span><span class="sub">PARTNERSHIP</span></span></div>
    <h2 class="abs heading center" style="left:0;right:0;top:12px">Heading Goes Here</h2>
    <p class="abs tiny center" style="left:48px;width:202px;top:27px">Add a short summary of the slide here so the reader knows what follows. Keep it to two brief lines and close with a clear note on the key idea.</p>
    <article class="pcard" style="left:27px"><div class="photo" role="img" aria-label="Photo of a tablet showing a chart on a desk"></div><p class="pc-head">Heading Goes Here</p><div class="row"><span class="dot"></span><span>Add a short point here in brief.</span></div><div class="row"><span class="dot"></span><span>Add a short point here in brief.</span></div><div class="row"><span class="dot"></span><span>Add a short point here in brief.</span></div></article>
    <article class="pcard" style="left:113px"><div class="photo" role="img" aria-label="Photo of a tablet showing a chart on a desk"></div><p class="pc-head">Heading Goes Here</p><div class="row"><span class="dot"></span><span>Add a short point here in brief.</span></div><div class="row"><span class="dot"></span><span>Add a short point here in brief.</span></div><div class="row"><span class="dot"></span><span>Add a short point here in brief.</span></div></article>
    <article class="pcard" style="left:199px"><div class="photo" role="img" aria-label="Photo of a tablet showing a chart on a desk"></div><p class="pc-head">Heading Goes Here</p><div class="row"><span class="dot"></span><span>Add a short point here in brief.</span></div><div class="row"><span class="dot"></span><span>Add a short point here in brief.</span></div><div class="row"><span class="dot"></span><span>Add a short point here in brief.</span></div></article>
    <footer class="foot"><span>© Quillmere 2025. All Rights Reserved.</span><span class="line"></span><span class="page">12</span></footer>
  </section>

  <!-- Stats rings -->
  <section class="slide light" style="left:345px;top:787px">
    <div class="mini-brand"><span class="brand-mark"></span><span class="brand-name"><span class="word">Quillmere</span><span class="sub">PARTNERSHIP</span></span></div>
    <h2 class="abs heading" style="left:17px;top:23px">Heading Goes Here</h2>
    <p class="abs tiny" style="left:17px;top:38px;width:96px">Add a short summary of the slide here so the reader can follow the key idea and see why it matters today.</p>
    <div class="abs" style="left:17px;top:68px;width:110px">
      <div style="display:flex;gap:6px;height:29px"><span class="num">1</span><div><p class="desc-title">Description Text</p><p class="desc" style="color:var(--muted)">Add a short line about this point here and a brief note.</p></div></div>
      <div style="display:flex;gap:6px;height:29px"><span class="num">2</span><div><p class="desc-title">Description Text</p><p class="desc" style="color:var(--muted)">Add a short line about this point here and a brief note.</p></div></div>
      <div style="display:flex;gap:6px"><span class="num">3</span><div><p class="desc-title">Description Text</p><p class="desc" style="color:var(--muted)">Add a short line about this point here and a brief note.</p></div></div>
    </div>
    <div class="abs" style="left:137px;top:26px;width:149px;height:118px;background:var(--ink);border-radius:5px"></div>
    <svg class="abs" style="left:137px;top:26px" width="149" height="118" viewBox="0 0 149 118" aria-label="Two progress rings showing 67 and 80 percent">
      <circle cx="39" cy="49" r="27" fill="none" stroke="#2d5a5d" stroke-width="3"/>
      <circle cx="39" cy="49" r="27" fill="none" stroke="#ffffff" stroke-width="3" stroke-dasharray="113.6 170" transform="rotate(-90 39 49)"/>
      <text x="39" y="53" text-anchor="middle" font-family="Red Hat Display, sans-serif" font-size="13" font-weight="600" fill="#fff">67%</text>
      <circle cx="111" cy="49" r="27" fill="none" stroke="#2d5a5d" stroke-width="3"/>
      <circle cx="111" cy="49" r="27" fill="none" stroke="#ffffff" stroke-width="3" stroke-dasharray="135.7 170" transform="rotate(-90 111 49)"/>
      <text x="111" y="53" text-anchor="middle" font-family="Red Hat Display, sans-serif" font-size="13" font-weight="600" fill="#fff">80%</text>
    </svg>
    <p class="abs tiny center" style="left:144px;top:97px;width:65px;font-size:3.2px">Add a short note here about this figure and what it shows.</p>
    <p class="abs tiny center" style="left:214px;top:97px;width:65px;font-size:3.2px">Add a short note here about this figure and what it shows.</p>
    <footer class="foot"><span>© Quillmere 2025. All Rights Reserved.</span><span class="line"></span><span class="page">13</span></footer>
  </section>

  <!-- Bar chart -->
  <section class="slide light" style="left:661px;top:787px">
    <div class="mini-brand"><span class="brand-mark"></span><span class="brand-name"><span class="word">Quillmere</span><span class="sub">PARTNERSHIP</span></span></div>
    <h2 class="abs heading center" style="left:0;right:0;top:18px">Heading Goes Here</h2>
    <p class="abs tiny center" style="left:48px;width:202px;top:33px">Add a short summary of the slide here so the reader knows what follows. Keep it to two brief lines and close with a clear note on the key idea.</p>
    <svg class="abs" style="left:16px;top:58px" width="140" height="86" viewBox="0 0 140 86" aria-label="Bar chart with three series across four categories" font-family="Red Hat Display, sans-serif" font-size="2.3" fill="#4f6264">
      <g stroke="#e3e7e7" stroke-width=".3">
        <line x1="8" y1="2" x2="138" y2="2"/><line x1="8" y1="14" x2="138" y2="14"/><line x1="8" y1="26" x2="138" y2="26"/><line x1="8" y1="38" x2="138" y2="38"/><line x1="8" y1="50" x2="138" y2="50"/><line x1="8" y1="62" x2="138" y2="62"/>
      </g>
      <line x1="8" y1="74" x2="138" y2="74" stroke="#9aa6a7" stroke-width=".4"/>
      <text x="4" y="3">6</text><text x="4" y="15">5</text><text x="4" y="27">4</text><text x="4" y="39">3</text><text x="4" y="51">2</text><text x="4" y="63">1</text><text x="4" y="75">0</text>
      <g>
        <rect x="15" y="22.4" width="5" height="51.6" fill="#0a3035"/><rect x="21" y="45.2" width="5" height="28.8" fill="#1f5558"/><rect x="27" y="50" width="5" height="24" fill="#e2550e"/>
        <rect x="46" y="21.2" width="5" height="52.8" fill="#0a3035"/><rect x="52" y="44" width="5" height="30" fill="#1f5558"/><rect x="58" y="50" width="5" height="24" fill="#e2550e"/>
        <rect x="77" y="32" width="5" height="42" fill="#0a3035"/><rect x="83" y="52.4" width="5" height="21.6" fill="#1f5558"/><rect x="89" y="38" width="5" height="36" fill="#e2550e"/>
        <rect x="108" y="20" width="5" height="54" fill="#0a3035"/><rect x="114" y="42.8" width="5" height="31.2" fill="#1f5558"/><rect x="120" y="14" width="5" height="60" fill="#e2550e"/>
      </g>
      <text x="23" y="79" text-anchor="middle">Category 1</text><text x="54" y="79" text-anchor="middle">Category 2</text><text x="85" y="79" text-anchor="middle">Category 3</text><text x="116" y="79" text-anchor="middle">Category 4</text>
    </svg>
    <div class="abs" style="left:183px;top:62px;width:105px">
      <div style="display:flex;gap:6px;height:29px"><span class="num ink">1</span><div><p class="desc-title">Description Text</p><p class="desc" style="color:var(--muted)">Add a short line about this point here and a brief note.</p></div></div>
      <div style="display:flex;gap:6px;height:29px"><span class="num ink">2</span><div><p class="desc-title">Description Text</p><p class="desc" style="color:var(--muted)">Add a short line about this point here and a brief note.</p></div></div>
      <div style="display:flex;gap:6px"><span class="num ink">3</span><div><p class="desc-title">Description Text</p><p class="desc" style="color:var(--muted)">Add a short line about this point here and a brief note.</p></div></div>
    </div>
    <footer class="foot"><span>© Quillmere 2025. All Rights Reserved.</span><span class="line"></span><span class="page">14</span></footer>
  </section>

  <!-- Table -->
  <section class="slide light" style="left:146px;top:975px">
    <div class="mini-brand"><span class="brand-mark"></span><span class="brand-name"><span class="word">Quillmere</span><span class="sub">PARTNERSHIP</span></span></div>
    <h2 class="abs heading" style="left:17px;top:19px">Heading Goes Here</h2>
    <div class="abs" style="left:17px;top:33px;width:20px;height:1px;background:var(--orange)"></div>
    <table class="grid">
      <thead><tr><th>Heading</th><th>Column Title 1</th><th>Column Title 2</th><th>Column Title 3</th><th>Column Title 4</th></tr></thead>
      <tbody>
        <tr><td class="rowhead">Row label here</td><td>Add a short note in this cell here in brief.</td><td>Add a short note in this cell here in brief.</td><td>Add a short note in this cell here in brief.</td><td>Add a short note in this cell here in brief.</td></tr>
        <tr><td class="rowhead">Row label here</td><td>Add a short note in this cell here in brief.</td><td>Add a short note in this cell here in brief.</td><td>Add a short note in this cell here in brief.</td><td>Add a short note in this cell here in brief.</td></tr>
        <tr><td class="rowhead">Row label here</td><td>Add a short note in this cell here in brief.</td><td>Add a short note in this cell here in brief.</td><td>Add a short note in this cell here in brief.</td><td>Add a short note in this cell here in brief.</td></tr>
        <tr><td class="rowhead">Row label here</td><td>Add a short note in this cell here in brief.</td><td>Add a short note in this cell here in brief.</td><td>Add a short note in this cell here in brief.</td><td>Add a short note in this cell here in brief.</td></tr>
        <tr><td class="rowhead">Row label here</td><td>Add a short note in this cell here in brief.</td><td>Add a short note in this cell here in brief.</td><td>Add a short note in this cell here in brief.</td><td>Add a short note in this cell here in brief.</td></tr>
      </tbody>
    </table>
    <footer class="foot"><span>© Quillmere 2025. All Rights Reserved.</span><span class="line"></span><span class="page">15</span></footer>
  </section>

  <!-- Thank you -->
  <section class="slide dark" style="left:468px;top:975px">
    <div class="abs brand" style="left:25px;top:22px"><span class="brand-mark"></span><span class="brand-name"><span class="word">Quillmere</span><span class="sub">PARTNERSHIP</span></span></div>
    <h2 class="abs" style="left:26px;top:78px;font-size:9px;font-weight:700">Contact Us</h2>
    <div class="abs" style="left:26px;top:97px">
      <p class="contact"><svg viewBox="0 0 16 16"><path d="M4 1.5l2.5 3-1.5 2a9 9 0 0 0 4.5 4.5l2-1.5 3 2.5-1.5 2.5C7 14 2 9 1.5 3.5z" fill="#fff"/></svg>Phone Number Goes Here</p>
      <p class="contact"><svg viewBox="0 0 16 16"><rect x="1.5" y="3.5" width="13" height="9" fill="#fff"/><path d="M1.5 3.5l6.5 5 6.5-5" fill="none" stroke="#0a3035" stroke-width="1.2"/></svg>E-Mail Address Goes Here</p>
      <p class="contact"><svg viewBox="0 0 16 16"><circle cx="8" cy="8" r="6" fill="none" stroke="#fff" stroke-width="1.4"/><path d="M2 8h12M8 2c-3 3-3 9 0 12M8 2c3 3 3 9 0 12" fill="none" stroke="#fff" stroke-width="1"/></svg>URL Address Goes Here</p>
    </div>
    <p class="abs thanks">Thank<br>You</p>
  </section>

</main>
</body>
</html>
```